Outdoor mass notification company needing business card design.

Our company name is Harrowgate Signal Systems Inc located in Amory Mississippi and we sell and maintain "Brantor" Mass Notification Sirens in the US. Outdoor sirens notify people of certain severe dangers such as tornados, severe thunderstorms, flooding, hurricanes and tsunamis. We also serve the oil and gas refining industries to warn of Chemical releases, fires, and lightning alerts.

Contact Information for Business Card

Name, title, cell number, email address

Requirements
Nice to have
• The Brantor logo and also the Mildvane logo.

```html
<!DOCTYPE html>
<html lang="en">
<head>
<meta charset="utf-8">
<title>Harrowgate Signal Systems – Business Card</title>
<link href="https://fonts.googleapis.com/css2?family=Cinzel:wght@700&family=Montserrat:wght@400;500&display=swap" rel="stylesheet">
<style>
  :root {
    --backdrop: #b9b9b9;
    --card-white: #ffffff;
    --brand-blue: #3b5673;
    --brand-blue-deep: #2e465f;
    --text-grey: #4a4a4a;
    --rule: #5e7690;
  }
  * { box-sizing: border-box; margin: 0; padding: 0; }
  html, body { width: 1200px; height: 802px; overflow: hidden; }
  body {
    background: var(--backdrop);
    font-family: "Montserrat", Arial, sans-serif;
    position: relative;
  }
  .card {
    position: absolute;
    top: 251px;
    width: 520px;
    height: 300px;
    border-radius: 26px;
    overflow: hidden;
  }
  .card--front { left: 50px; background: var(--card-white); }
  .card--back { left: 630px; background: var(--brand-blue); }

  .front-band {
    position: absolute;
    left: 0; bottom: 0;
    width: 100%; height: 16px;
  }
  .wordmark {
    position: absolute;
    font-family: "Cinzel", Georgia, serif;
    font-weight: 700;
    line-height: 1.05;
    color: var(--brand-blue);
    display: flex;
    align-items: center;
    gap: 10px;
  }
  .wordmark__dot {
    width: 14px; height: 14px;
    border-radius: 50%;
    background: var(--brand-blue);
    flex: none;
  }
  .card--front .wordmark {
    top: 34px; right: 34px;
    font-size: 21px;
    text-align: left;
  }
  .person {
    position: absolute;
    left: 34px; top: 126px;
  }
  .person__name {
    font-family: "Cinzel", Georgia, serif;
    font-weight: 700;
    font-size: 20px;
    color: var(--brand-blue);
    letter-spacing: 0.5px;
  }
  .person__title {
    font-size: 13px;
    color: var(--text-grey);
    margin-top: 2px;
  }
  .divider {
    position: absolute;
    left: 34px; right: 34px; top: 180px;
    height: 1px;
    background: var(--rule);
  }
  .contacts {
    position: absolute;
    left: 34px; top: 192px;
    list-style: none;
    font-size: 13px;
    color: var(--text-grey);
  }
  .contacts li {
    display: flex; align-items: center; gap: 8px;
    height: 21px;
  }
  .contacts svg { width: 11px; height: 11px; fill: var(--brand-blue); flex: none; }
  .contacts .accent { color: var(--brand-blue); }
  .address {
    position: absolute;
    right: 34px; top: 196px;
    text-align: right;
    font-size: 12.5px;
    line-height: 1.55;
    color: var(--text-grey);
  }

  .card--back .wordmark {
    left: 0; right: 0; top: 0; bottom: 0;
    justify-content: center;
    font-size: 34px;
    color: var(--brand-blue-deep);
  }
  .card--back .wordmark__dot {
    width: 20px; height: 20px;
    background: var(--brand-blue-deep);
  }
</style>
</head>
<body>

<section class="card card--front" aria-label="Business card front">
  <svg class="front-band" viewBox="0 0 520 16" preserveAspectRatio="none" aria-hidden="true">
    <polygon points="0,0 300,0 316,16 0,16" fill="var(--brand-blue)"/>
  </svg>

  <div class="wordmark">
    <span class="wordmark__dot"></span>
    <span>Harrowgate<br>Signal Systems</span>
  </div>

  <div class="person">
    <p class="person__name">DALE VICKERY</p>
    <p class="person__title">CEO/Founder</p>
  </div>

  <div class="divider"></div>

  <ul class="contacts">
    <li>
      <svg viewBox="0 0 24 24"><path d="M6.6 10.8a15.1 15.1 0 0 0 6.6 6.6l2.2-2.2a1 1 0 0 1 1-.25 11.4 11.4 0 0 0 3.6.57 1 1 0 0 1 1 1V20a1 1 0 0 1-1 1A17 17 0 0 1 3 4a1 1 0 0 1 1-1h3.5a1 1 0 0 1 1 1c0 1.25.2 2.45.57 3.570a1 1 0 0 1-.25 1z"/></svg>
      (662)555-0147
    </li>
    <li>
      <svg viewBox="0 0 24 24"><path d="M2 5h20v14H2zm2 2v.5l8 5 8-5V7z"/></svg>
      info@harrowgatesignal.com
    </li>
    <li>
      <svg viewBox="0 0 24 24"><circle cx="12" cy="12" r="10"/></svg>
      <span>www.<span class="accent">harrowgatesignal</span>.com</span>
    </li>
  </ul>

  <p class="address">214 Front Street North<br>Amory, Mississippi 38821</p>
</section>

<section class="card card--back" aria-label="Business card back">
  <div class="wordmark">
    <span class="wordmark__dot"></span>
    <span>Harrowgate<br>Signal Systems</span>
  </div>
</section>

</body>
</html>
```